Modern Design Business Card industrial maintenance company

Business card design for Company named Brookvale Equipment Services

Target Market(s)

Industrial

Industry/Entity Type

Maintenance and repair

Contact Information for Business Card

Place holder for address, office phone, mobile number and email

Requirements
Must have
• Clean modern look
Nice to have
• N/a

```html
<!DOCTYPE html>
<html lang="en">
<head>
<meta charset="utf-8">
<title>Brookvale Equipment Services – Business Card</title>
<link href="https://fonts.googleapis.com/css2?family=Michroma&family=Poppins:wght@400&display=swap" rel="stylesheet">
<style>
  :root {
    --stage: #1e1e1e;
    --card-dark: #0c0c0c;
    --card-light: #ffffff;
    --ink: #111111;
    --silver: #b9b9b9;
    --silver-soft: #8a8a8a;
  }
  html, body { margin: 0; padding: 0; overflow: hidden; }
  body {
    width: 1200px; height: 1200px;
    background: var(--stage);
    position: relative;
  }
  .card {
    position: absolute;
    left: 220px;
    width: 760px; height: 434px;
    border-radius: 22px;
    box-sizing: border-box;
  }
  .card-back {
    top: 150px;
    background: linear-gradient(160deg, #1a1a1a 0%, var(--card-dark) 60%);
    display: flex; flex-direction: column; align-items: center; justify-content: center;
  }
  .brand-mark {
    width: 120px; height: 120px;
    border: 5px solid var(--silver);
    border-radius: 50%;
    box-sizing: border-box;
    margin-bottom: 22px;
  }
  .brand-name {
    font-family: "Michroma", sans-serif;
    color: var(--silver);
    text-align: center;
    letter-spacing: 4px;
    line-height: 1.5;
  }
  .brand-name .line-1 { display: block; font-size: 34px; }
  .brand-name .line-2 { display: block; font-size: 15px; letter-spacing: 7px; }

  .card-front {
    top: 620px;
    background: var(--card-light);
    color: var(--ink);
  }
  .holder {
    position: absolute; left: 56px; top: 44px;
    font-family: "Michroma", sans-serif;
  }
  .holder-name { font-size: 26px; letter-spacing: 3px; margin: 0; }
  .holder-role { font-size: 15px; letter-spacing: 4px; margin: 6px 0 0; }

  .contact {
    position: absolute; left: 56px; bottom: 44px;
    font-family: "Poppins", sans-serif;
    font-size: 19px; line-height: 1.45;
    list-style: none; margin: 0; padding: 0;
  }
  .contact li { display: flex; align-items: center; gap: 10px; }
  .contact svg { width: 18px; height: 18px; flex: none; }
  .contact .address { padding-left: 0; margin-top: 8px; display: block; }

  .front-mark {
    position: absolute; right: 70px; top: 100px;
    width: 260px; height: 260px;
    border: 9px solid var(--ink);
    border-radius: 50%;
    box-sizing: border-box;
    display: flex; align-items: center; justify-content: center;
    font-family: "Michroma", sans-serif;
    font-size: 24px; letter-spacing: 2px;
  }
</style>
</head>
<body>
  <section class="card card-back">
    <div class="brand-mark"></div>
    <div class="brand-name">
      <span class="line-1">BROOKVALE</span>
      <span class="line-2">EQUIPMENT SERVICES</span>
    </div>
  </section>

  <section class="card card-front">
    <div class="holder">
      <h1 class="holder-name">DANIEL REYES</h1>
      <p class="holder-role">CEO/FOUNDER</p>
    </div>

    <ul class="contact">
      <li>
        <svg viewBox="0 0 24 24"><path d="M6.6 10.8a15 15 0 0 0 6.6 6.6l2.2-2.2a1 1 0 0 1 1-.25 11.4 11.4 0 0 0 3.6.57 1 1 0 0 1 1 1V20a1 1 0 0 1-1 1A17 17 0 0 1 3 4a1 1 0 0 1 1-1h3.5a1 1 0 0 1 1 1c0 1.25.2 2.45.57 3.57a1 1 0 0 1-.25 1z" fill="#111"/></svg>
        555 014 2380
      </li>
      <li>
        <svg viewBox="0 0 24 24"><rect x="6" y="2" width="12" height="20" rx="2" fill="none" stroke="#111" stroke-width="2"/><circle cx="12" cy="18" r="1.2" fill="#111"/></svg>
        555 014 2380
      </li>
      <li>
        <svg viewBox="0 0 24 24"><rect x="2" y="5" width="20" height="14" fill="#111"/><path d="M2 5l10 8 10-8" fill="none" stroke="#fff" stroke-width="1.5"/></svg>
        daniel@brookvaleequip.com
      </li>
      <li class="address">P.O. Box 417 2190 Harlow Rd<br>Millbrook Ohio 45012</li>
    </ul>

    <div class="front-mark">BROOKVALE</div>
  </section>
</body>
</html>
```